依頼詳細
お好み焼き屋さんのTOPページのみのデザインをお願いしたいです。
コロナで減少したお客様を呼び戻すために試行錯誤しながら、このたびラーメンも提供することになりましたので、メインはお好み焼き屋さんですが、ラーメンも始めました!という画像付きで告知したいです。

集客を目的としたサイトです。
ターゲットは。お腹が空いた人になります!

レイアウト構成
・ヘッダー(ロゴのみ)
・TOP画像(画像はまだないのでフリーのもので大丈夫です)
・TOPページは画像だけでなくインパクトある感じを希望です(ザックリですみません。)
・お知らせ(3行程度)
・メニュー(テキストのみ)
・店舗情報(2店舗)テキスト
・フッター(下層ページないのでコピーライトぐらいでしょうか)
という構成です。
どこかにツマミドリと味ノートにリンクするボタンが欲しいです。
まだ素材がないため仮のフリー画像で構いません。

初心者の方でも大丈夫です!
今回は予算の都合上、低価格になってしまいましたがデザインのフィーリングが合う方は今後もご依頼する可能性があります!
サイトURL
ページ数
1ページ
希望イメージ
シンプル 複雑
単色 カラフル
暗い 明るい
日常 高級
遊び心 厳粛
未来的 伝統的
女性的 男性的
希望する色
無彩色系
納品ファイル
• 高解像度JPG (.jpg)
• イラストレーター形式 (.ai)
• フォトショップ形式 (.psd)
• PNG形式 (.png)
補足説明
納品はできれば、XDが希望です。
難しい場合はご相談ください。

お客様のイメージに一番近かったため選びました!

この度は、とても素晴らしいデザインのご提案をいただきまして誠にありがとうございました。
どれも捨てがたいデザインなのですが、一番イメージに近いものを選びました。
また、機会がございましたら、ご依頼をさせていただければと思います。
どうぞよろしくお願いいたします。

```html
<!DOCTYPE html>
<html lang="ja">
<head>
<meta charset="utf-8">
<title>鉄板 こなや｜お好み焼き・ラーメン</title>
<link href="https://fonts.googleapis.com/css2?family=Shippori+Mincho:wght@400;600&display=swap" rel="stylesheet">
<style>
:root{
  --brown:#3a2414;
  --brown-deep:#2b190c;
  --cream:#f3ece1;
  --ink:#3a2a1e;
  --line:#cbbfae;
  --gold:#c9a86a;
  --white:#ffffff;
}
*{margin:0;padding:0;box-sizing:border-box}
html,body{width:1200px;height:2856px;overflow:hidden}
body{font-family:"Shippori Mincho",serif;color:var(--ink);background:var(--white);position:relative}
.abs{position:absolute}

/* hero */
.hero{top:0;left:0;width:1200px;height:720px;background:radial-gradient(ellipse at 30% 55%,#d9b98a 0%,#a8763f 30%,#5a3a22 60%,#2a1a10 100%)}
.header-bar{top:0;left:0;width:1200px;height:44px;display:flex;align-items:center;color:var(--white);font-size:15px}
.header-name{position:absolute;left:150px;top:12px;font-size:16px;letter-spacing:.1em}
.header-tel{position:absolute;left:330px;top:14px;font-size:14px;letter-spacing:.08em}
.link-btn{position:absolute;top:6px;height:34px;border:1px solid rgba(255,255,255,.8);color:var(--white);font-size:14px;display:flex;align-items:center;justify-content:center;gap:8px;letter-spacing:.1em;background:rgba(0,0,0,.35)}
.link-btn::before{content:"";width:8px;height:8px;background:var(--white)}
.btn-tsumami{left:780px;width:160px}
.btn-aji{left:960px;width:200px}
.hero-panel{top:0;left:440px}
.hero-brand{top:150px;left:440px;width:280px;text-align:center;color:var(--white);font-size:24px;font-weight:600;letter-spacing:.2em}
.hero-copy{top:252px;left:440px;width:280px;text-align:center;color:var(--white);font-size:20px;letter-spacing:.12em;white-space:nowrap}
.ramen-photo{top:320px;left:520px;width:120px;height:120px;border-radius:50%;background:radial-gradient(circle,#e8c98a 0%,#b57b3a 55%,#2a1a10 100%)}
.hero-logo{top:520px;left:930px;width:140px;text-align:center;color:var(--white);font-size:18px;letter-spacing:.15em}
.hero-logo::before{content:"";display:block;width:12px;height:12px;background:var(--white);margin:0 auto 10px}

/* news */
.news-bg{top:720px;left:0}
.news-title{top:748px;left:72px;color:var(--white);font-size:26px;letter-spacing:.15em}
.news-list{top:740px;left:240px;width:680px;list-style:none}
.news-list li{height:60px;border-bottom:1px solid rgba(255,255,255,.35);color:var(--white);font-size:13px;display:flex;align-items:center;gap:24px;letter-spacing:.06em}

/* menu */
.section-head{left:0;width:1200px;text-align:center;font-size:28px;letter-spacing:.4em}
.menu-head{top:1020px;color:var(--ink)}
.menu-head::before,.menu-head::after{content:"";display:inline-block;width:60px;height:1px;background:var(--ink);vertical-align:middle;margin:0 20px}
.menu-cols{top:1190px;left:176px;display:flex;gap:27px}
.menu-col{width:26px;display:flex;flex-direction:column;align-items:center}
.vt{writing-mode:vertical-rl;letter-spacing:.15em}
.dish{font-size:17px;height:150px}
.price{font-size:15px;margin-top:20px}
.cat{left:980px;display:flex;align-items:flex-start;gap:10px}
.cat-label{font-size:20px}
.cat-okonomi{top:1220px}
.cat-ramen{top:1590px}
.cat-icon{width:20px;height:20px;border-radius:50%;background:var(--ink)}
.menu-rule{top:1540px;left:180px;width:840px;height:1px;background:var(--line)}
.ramen-cols{top:1600px;left:826px;display:flex;gap:20px}
.ramen-cols .dish{height:70px}

/* shops */
.shop-bg{top:1840px;left:0}
.shop-head{top:1972px;left:575px;color:var(--white);font-size:30px;writing-mode:vertical-rl;letter-spacing:.3em;font-weight:600}
.shop-card{top:2180px;width:440px;height:520px;border:1px solid rgba(255,255,255,.6);color:var(--white);padding:24px 30px}
.card-main{left:140px}
.card-branch{left:620px}
.shop-name{text-align:center;font-size:22px;letter-spacing:.4em;margin-bottom:34px}
.shop-name::before,.shop-name::after{content:"—";margin:0 10px;font-size:16px}
.shop-info{display:grid;grid-template-columns:80px 1fr;row-gap:12px;font-size:13px;line-height:1.7;letter-spacing:.04em}
.shop-info dt{color:var(--gold)}
.map{margin-top:30px;width:100%;height:230px;background:linear-gradient(135deg,#e9e5dc,#cfd8e3 60%,#9fc0e0)}
.to-top{top:2726px;left:966px;width:60px;height:44px;border:1px solid rgba(255,255,255,.7);color:var(--white);font-size:13px;display:flex;align-items:center;justify-content:center;letter-spacing:.1em}
.copyright{top:2816px;left:0;width:1200px;text-align:center;color:var(--white);font-size:11px;letter-spacing:.12em;opacity:.85}
</style>
</head>
<body>

<div class="abs hero" role="img" aria-label="鉄板で焼き上がったお好み焼きの写真"></div>
<svg class="abs hero-panel" width="280" height="680" viewBox="0 0 280 680"><path d="M0 0H280V600Q210 600 180 640Q140 690 100 640Q70 600 0 600Z" fill="var(--brown)"/></svg>
<div class="abs hero-brand">鉄板 こなや</div>
<div class="abs hero-copy">ラーメン、はじめました</div>
<div class="abs ramen-photo" role="img" aria-label="ラーメンの写真"></div>
<div class="abs hero-logo">鉄板 こなや</div>

<header class="abs header-bar">
  <span class="header-name">鉄板 こなや</span>
  <span class="header-tel">☎ 03-1234-5678</span>
  <a class="link-btn btn-tsumami">ツマミドリ</a>
  <a class="link-btn btn-aji">味ノート</a>
</header>

<svg class="abs news-bg" width="1200" height="360" viewBox="0 0 1200 360"><path d="M0 0H1200V200Q1060 180 960 210Q880 240 820 280Q760 320 660 300Q560 280 420 270Q240 255 0 290Z" fill="var(--brown)"/></svg>
<h2 class="abs news-title">おしらせ</h2>
<ul class="abs news-list">
  <li><span>2024.11.25</span><span>ラーメンの提供を開始しました（平日11:00〜14:00）</span></li>
  <li><span>2024.11.14</span><span>12月の営業日についてのお知らせ</span></li>
  <li><span>2024.11.14</span><span>冬の限定メニューはじめました</span></li>
</ul>

<h2 class="abs section-head menu-head">メニュー</h2>
<div class="abs menu-cols">
  <div class="menu-col"><span class="vt dish">豚玉</span><span class="vt price">700円（税込）</span></div>
  <div class="menu-col"><span class="vt dish">いか玉</span><span class="vt price">700円（税込）</span></div>
  <div class="menu-col"><span class="vt dish">えび玉</span><span class="vt price">750円（税込）</span></div>
  <div class="menu-col"><span class="vt dish">牛すじ</span><span class="vt price">800円（税込）</span></div>
  <div class="menu-col"><span class="vt dish">もち明太</span><span class="vt price">800円（税込）</span></div>
  <div class="menu-col"><span class="vt dish">チーズ</span><span class="vt price">750円（税込）</span></div>
  <div class="menu-col"><span class="vt dish">ミックス</span><span class="vt price">900円（税込）</span></div>
  <div class="menu-col"><span class="vt dish">ねぎ焼き</span><span class="vt price">700円（税込）</span></div>
  <div class="menu-col"><span class="vt dish">キムチ</span><span class="vt price">750円（税込）</span></div>
  <div class="menu-col"><span class="vt dish">塩だれ</span><span class="vt price">700円（税込）</span></div>
  <div class="menu-col"><span class="vt dish">広島風</span><span class="vt price">900円（税込）</span></div>
  <div class="menu-col"><span class="vt dish">モダン</span><span class="vt price">850円（税込）</span></div>
  <div class="menu-col"><span class="vt dish">特製</span><span class="vt price">1000円（税込）</span></div>
  <div class="menu-col"><span class="vt dish">野菜玉</span><span class="vt price">650円（税込）</span></div>
  <div class="menu-col"><span class="vt dish">焼きそば</span><span class="vt price">700円（税込）</span></div>
</div>
<div class="abs cat cat-okonomi"><span class="vt cat-label">お好み焼き</span><span class="cat-icon"></span></div>
<div class="abs menu-rule"></div>
<div class="abs ramen-cols">
  <div class="menu-col"><span class="vt dish">豚骨</span><span class="vt price">700円（税込）</span></div>
  <div class="menu-col"><span class="vt dish">味噌</span><span class="vt price">700円（税込）</span></div>
  <div class="menu-col"><span class="vt dish">醤油</span><span class="vt price">700円（税込）</span></div>
</div>
<div class="abs cat cat-ramen"><span class="vt cat-label">ラーメン</span><span class="cat-icon"></span></div>

<svg class="abs shop-bg" width="1200" height="1016" viewBox="0 0 1200 1016"><path d="M0 90Q180 40 380 80Q600 120 820 70Q1020 30 1200 60V1016H0Z" fill="var(--brown)"/></svg>
<h2 class="abs shop-head">店舗情報</h2>

<section class="abs shop-card card-main">
  <h3 class="shop-name">本店</h3>
  <dl class="shop-info">
    <dt>営業時間</dt><dd>11:00〜14:00 ／ 18:00〜22:00<br>（定休日：月曜日）</dd>
    <dt>電話番号</dt><dd>03-1234-5678</dd>
    <dt>所在地</dt><dd>〒123-4567<br>東京都架空区見本町1-2-3</dd>
  </dl>
  <div class="map" role="img" aria-label="本店周辺の地図"></div>
</section>

<section class="abs shop-card card-branch">
  <h3 class="shop-name">二号店</h3>
  <dl class="shop-info">
    <dt>営業時間</dt><dd>11:00〜14:00 ／ 18:00〜22:00<br>（定休日：火曜日）</dd>
    <dt>電話番号</dt><dd>03-1234-5679</dd>
    <dt>所在地</dt><dd>〒123-4568<br>東京都架空区見本町4-5-6</dd>
  </dl>
  <div class="map" role="img" aria-label="二号店周辺の地図"></div>
</section>

<a class="abs to-top">TOP</a>
<footer class="abs copyright">© KONAYA All rights reserved.</footer>

</body>
</html>
```